PRVKA Membership Flyer

• 1 Page Flyer promoting PRVKA Membership Drive
• I have attached our organization brochure for organizational info
• Please include the same PRVKA logo as seen in brochure
• Membership $20/year
• Contact Tomas Weller to Join at wellto42@learners.brvx.edu
INCLUDE Organization Advisers
Dr. Rostam Velani NPV School of Dental Medicine (photo from attached brochure)
Dr. Felix Oyo NPV Tarrow School of Medicine (Photo from Attached brochure)

Member Benefits
• Access to exclusive Interdisciplinary world-renowned guest speaker presentations
• Mentorship for residencies / Oral Medicine Fellowship for nondental healthcare students
• Shadowing opportunities with Oral Medicine Specialist
• Participate in research journal club
• Clinical Research, Case Reports and Lindqvar Fellowship opportunities
• Exclusive Lunch and Learn Invitations
• 10% Discount to Special Events Sponsored by PRVKA
• Enhance your Interdisciplinary resource network

Renew or Join PRVKA by August 30th and be entered in a free raffle for the chance to win one of 3 drawings
$50 Zorel Gift Card
2x $25 Plumfield Gift Card

Target Market(s)

Students

Requirements
Must have
• Must use the PRVKA Logo from brochure, Member Benefits • Access to exclusive Interdisciplinary world-renowned guest speaker presentations • Mentorship for residencies / Oral Medicine Fellowship for nondental healthcare students • Shadowing opportunities with Oral Medicine Specialist • Participate in research journal club • Clinical Research, Case Reports and Lindqvar Fellowship opportunities • Exclusive Lunch and Learn Invitations • 10% Discount to Special Events Sponsored by PRVKA • Enhance your Interdisciplinary resource network Renew or Join PRVKA by August 30th and be entered in a free raffle for the chance to win one of 3-4 drawings $50 Zorel Gift Card 2x $25 Plumfield Gift Card
Nice to have
• Similar design background to brochure attached,

```html
<!DOCTYPE html>
<html lang="en">
<head>
<meta charset="utf-8">
<title>PRVKA Membership Flyer</title>
<link rel="stylesheet" href="https://fonts.googleapis.com/css2?family=Libre+Baskerville:wght@400;700&family=Raleway:wght@500;600&display=swap">
<style>
  :root {
    --purple: #4a1f84;
    --purple-dark: #351468;
    --gold: #c9a52a;
    --gold-dark: #8f7213;
    --gold-light: #f3d63a;
    --ink: #1d1d1f;
    --paper: #ffffff;
    --stage: #38393b;
    --sketch: #e6e6e8;
  }
  * { margin: 0; padding: 0; box-sizing: border-box; }
  html, body { width: 1200px; height: 2336px; overflow: hidden; background: var(--stage); }
  .flyer {
    position: absolute; left: 0; top: 320px; width: 1200px; height: 1697px;
    background: var(--paper); overflow: hidden;
    font-family: "Raleway", sans-serif; color: var(--ink);
  }
  .sketch-bg {
    position: absolute; left: 0; top: 560px; width: 1200px; height: 1060px;
    background: radial-gradient(ellipse at 70% 50%, var(--sketch) 0%, #f2f2f3 45%, rgba(255,255,255,0) 75%);
  }
  .decor { position: absolute; left: 0; top: 0; width: 1200px; height: 1000px; }
  .hall-photo {
    position: absolute; left: 581px; top: -110px; width: 786px; height: 786px; border-radius: 50%;
    background: linear-gradient(160deg, #d9d5cf 0%, #b9b3aa 35%, #8c7a62 60%, #c99a5e 85%, #a57a46 100%);
  }
  .wordmark {
    position: absolute; left: 100px; top: 100px; width: 440px; text-align: center;
    font-family: "Raleway", sans-serif; font-weight: 600; font-size: 96px; line-height: 1.05;
    color: var(--purple);
  }
  .price { position: absolute; left: 82px; top: 425px; font-family: "Libre Baskerville", serif; }
  .price-label { font-size: 76px; line-height: 1.05; color: var(--ink); }
  .price-amount { font-size: 96px; font-weight: 700; line-height: 1; color: var(--gold); }
  .adviser {
    position: absolute; border-radius: 50%; border: 10px solid #fff;
    box-shadow: 0 4px 16px rgba(0,0,0,.35); overflow: hidden;
    background: radial-gradient(circle at 50% 40%, #b9a08a 0%, #8e7664 40%, #7a8188 70%, #9aa0a6 100%);
  }
  .adviser-name {
    position: absolute; left: 0; right: 0; bottom: 0; height: 17%; background: var(--purple);
    color: #fff; font-size: 21px; text-align: center; padding-top: 8px;
  }
  .adviser--oyo { left: 553px; top: 473px; width: 288px; height: 288px; }
  .adviser--velani { left: 782px; top: 591px; width: 366px; height: 366px; }
  .benefits-title {
    position: absolute; left: 74px; top: 800px; font-family: "Libre Baskerville", serif;
    font-weight: 700; font-size: 68px; color: var(--purple);
  }
  .benefits { position: absolute; left: 86px; top: 900px; list-style: none; }
  .benefit { position: relative; padding-left: 62px; font-size: 27px; font-weight: 500; line-height: 33px; margin-bottom: 20px; }
  .benefit svg { position: absolute; left: 0; top: 2px; width: 36px; height: 36px; }
  .benefit--tight { margin-bottom: 18px; }
  .promo {
    position: absolute; top: 1390px; height: 190px; border-radius: 26px;
    background: linear-gradient(180deg, var(--gold) 0%, #a98a1c 55%, var(--gold-dark) 100%);
    box-shadow: 0 6px 14px rgba(0,0,0,.25);
    font-family: "Libre Baskerville", serif; font-weight: 700;
  }
  .promo--raffle { left: 77px; width: 500px; padding: 22px 0 0 34px; font-size: 28px; line-height: 37px; color: #fff; }
  .promo--raffle em { font-style: normal; color: var(--gold-light); }
  .promo--prizes { left: 622px; width: 500px; padding: 22px 0 0 76px; font-size: 35px; line-height: 48px; color: #fff; }
  .prize { position: relative; white-space: nowrap; }
  .prize svg { position: absolute; left: -56px; top: 7px; width: 32px; height: 32px; }
  .contact-bar {
    position: absolute; left: 0; bottom: 0; width: 1200px; height: 77px;
    background: linear-gradient(180deg, var(--purple) 0%, var(--purple-dark) 100%);
    display: flex; align-items: center; justify-content: center; gap: 14px;
  }
  .contact-label { font-family: "Libre Baskerville", serif; font-weight: 700; font-size: 34px; color: var(--gold-light); }
  .contact-mail { font-size: 34px; font-weight: 600; color: #fff; }
  .contact-bar svg { width: 32px; height: 24px; }
</style>
</head>
<body>
<svg width="0" height="0" style="position:absolute">
  <defs>
    <symbol id="tick" viewBox="0 0 36 36">
      <circle cx="17" cy="19" r="14" fill="none" stroke="currentColor" stroke-width="2.2"/>
      <path d="M10 18l6 7L33 4" fill="none" stroke="currentColor" stroke-width="2.6" stroke-linecap="round" stroke-linejoin="round"/>
    </symbol>
  </defs>
</svg>

<main class="flyer">
  <div class="sketch-bg" role="img" aria-label="Faint pencil anatomical drawing of a human skull and shoulder muscles"></div>
  <div class="hall-photo" role="img" aria-label="Photo of students seated in a lecture hall listening to a presentation"></div>

  <svg class="decor" viewBox="0 0 1200 1000">
    <circle cx="974" cy="283" r="404" fill="none" stroke="var(--gold)" stroke-width="14"/>
    <path d="M40 520 C130 760 420 820 700 700 C470 765 210 720 40 520 Z" fill="var(--gold)"/>
  </svg>

  <div class="wordmark">NPV<br>PRVKA</div>

  <div class="price">
    <div class="price-label">Membership</div>
    <div class="price-amount">$20/year</div>
  </div>

  <figure class="adviser adviser--oyo" role="img" aria-label="Portrait photo of Dr. Felix Oyo">
    <figcaption class="adviser-name">Dr. Felix Oyo</figcaption>
  </figure>
  <figure class="adviser adviser--velani" role="img" aria-label="Portrait photo of Dr. Rostam Velani">
    <figcaption class="adviser-name">Dr. Rostam Velani</figcaption>
  </figure>

  <h2 class="benefits-title">Member Benefits</h2>
  <ul class="benefits">
    <li class="benefit"><svg><use href="#tick"/></svg>Access to exclusive Interdisciplinary<br>world-renowned guest speaker presentations</li>
    <li class="benefit"><svg><use href="#tick"/></svg>Mentorship for residencies / Oral Medicine Fellowship<br>for nondental healthcare students</li>
    <li class="benefit"><svg><use href="#tick"/></svg>Clinical Research, Case Reports and Lindqvar Fellowship opportunities</li>
    <li class="benefit"><svg><use href="#tick"/></svg>Shadowing opportunities with Oral Medicine Specialist</li>
    <li class="benefit"><svg><use href="#tick"/></svg>Participate in research journal club</li>
    <li class="benefit benefit--tight"><svg><use href="#tick"/></svg>Exclusive Lunch and Learn Invitations</li>
    <li class="benefit benefit--tight"><svg><use href="#tick"/></svg>10% Discount to Special Events Sponsored by PRVKA</li>
    <li class="benefit"><svg><use href="#tick"/></svg>Enhance your Interdisciplinary resource network</li>
  </ul>

  <div class="promo promo--raffle">
    Renew or Join PRVKA by<br><em>August 30th</em> and be entered<br>in a <em>free raffle for the chance</em><br><em>to win one of 3 drawings</em>
  </div>
  <div class="promo promo--prizes">
    <div class="prize"><svg style="color:#fff"><use href="#tick"/></svg>$50 Zorel Gift Card</div>
    <div class="prize"><svg style="color:#fff"><use href="#tick"/></svg>2x $25 Plumfield</div>
    <div class="prize">Gift Card</div>
  </div>

  <footer class="contact-bar">
    <span class="contact-label">Contact Tomas Weller to Join at</span>
    <svg viewBox="0 0 32 24"><rect x="1" y="1" width="30" height="22" fill="var(--gold-light)"/><path d="M1 1l15 12L31 1" fill="none" stroke="var(--purple)" stroke-width="2"/></svg>
    <span class="contact-mail">wellto42@learners.brvx.edu</span>
  </footer>
</main>
</body>
</html>
```